Providing Back Office Solutions to Financial Advisors and Attorney Needs a Business Card Design

Need a Business Card Design that speaks to Financial Advisor and Attorneys. Some of the word that come to mind is Clean/Simple & Futuristic.

Industry/Entity Type

Business

```html
<!DOCTYPE html>
<html lang="en">
<head>
<meta charset="utf-8">
<title>Nexora Back Office Solutions – Business Card</title>
<link href="https://fonts.googleapis.com/css2?family=Roboto:wght@400;500&display=swap" rel="stylesheet">
<style>
  :root {
    --page-bg: #e9e6e1;
    --card-white: #f7f8fa;
    --card-mist: #e6ebf1;
    --brand-blue: #1f3f8c;
    --navy-deep: #0f2350;
    --navy: #1b3a78;
    --ocean: #1556a8;
    --silver: #d9d4cf;
    --contact-text: #dcd3c6;
  }
  * { margin: 0; padding: 0; box-sizing: border-box; }
  html, body { width: 1200px; height: 970px; overflow: hidden; }
  body {
    background: var(--page-bg);
    font-family: "Roboto", Arial, sans-serif;
    position: relative;
  }
  .business-card {
    position: absolute;
    left: 80px;
    top: 188px;
    width: 1040px;
    height: 594px;
    background: linear-gradient(160deg, var(--card-white) 0%, var(--card-mist) 100%);
    overflow: hidden;
    box-shadow: 0 18px 40px rgba(40, 40, 60, 0.22);
  }
  .card-wave { position: absolute; inset: 0; }
  .brand {
    position: absolute;
    left: 50px;
    top: 112px;
    display: flex;
    align-items: stretch;
  }
  .brand-rule {
    width: 2px;
    background: var(--brand-blue);
    margin-right: 18px;
  }
  .brand-name {
    font-size: 66px;
    font-weight: 500;
    letter-spacing: 5px;
    color: var(--brand-blue);
    line-height: 1;
  }
  .brand-tagline {
    margin-top: 16px;
    font-size: 24px;
    font-weight: 400;
    color: var(--brand-blue);
    letter-spacing: 0.3px;
  }
  .person {
    position: absolute;
    right: 42px;
    top: 342px;
    text-align: right;
    color: var(--contact-text);
  }
  .person-name { font-size: 30px; font-weight: 500; letter-spacing: 0.5px; }
  .person-role { font-size: 23px; margin-top: 2px; }
  .contact-list {
    position: absolute;
    right: 42px;
    top: 445px;
    list-style: none;
    color: var(--contact-text);
    font-size: 23px;
  }
  .contact-item {
    display: flex;
    justify-content: flex-end;
    align-items: center;
    gap: 12px;
    height: 35px;
  }
  .contact-icon { width: 30px; height: 30px; flex: none; }
</style>
</head>
<body>
  <div class="business-card">
    <svg class="card-wave" width="1040" height="594" viewBox="0 0 1040 594" aria-hidden="true">
      <defs>
        <linearGradient id="navyBand" x1="0" y1="0" x2="1" y2="0">
          <stop offset="0" stop-color="#23355e"/>
          <stop offset="0.6" stop-color="#14306a"/>
          <stop offset="1" stop-color="#0e3d8a"/>
        </linearGradient>
        <linearGradient id="oceanBand" x1="0" y1="0" x2="0" y2="1">
          <stop offset="0" stop-color="#1a5cb0"/>
          <stop offset="0.55" stop-color="#174f96"/>
          <stop offset="1" stop-color="#0c2248"/>
        </linearGradient>
      </defs>
      <path d="M0,425 C320,405 720,310 1040,53 L1040,594 L0,594 Z" fill="url(#navyBand)"/>
      <path d="M0,535 C350,470 700,330 920,160 C960,125 1000,95 1040,70 L1040,594 L0,594 Z" fill="url(#oceanBand)"/>
      <path d="M0,535 C350,470 700,330 920,160" fill="none" stroke="var(--silver)" stroke-width="3"/>
    </svg>

    <div class="brand">
      <div class="brand-rule"></div>
      <div class="brand-text">
        <div class="brand-name">NEXORA</div>
        <div class="brand-tagline">BACK OFFICE SOLUTIONS</div>
      </div>
    </div>

    <div class="person">
      <div class="person-name">JORDAN AVERY</div>
      <div class="person-role">Founder</div>
    </div>

    <ul class="contact-list">
      <li class="contact-item">
        <span>(555) 214-0387</span>
        <svg class="contact-icon" viewBox="0 0 30 30" aria-label="Phone">
          <circle cx="15" cy="15" r="13" fill="none" stroke="#e6e6e6" stroke-width="1.6"/>
          <rect x="10.5" y="7.5" width="9" height="15" rx="1.5" fill="none" stroke="#e6e6e6" stroke-width="1.6"/>
          <line x1="14" y1="19.5" x2="16" y2="19.5" stroke="#e6e6e6" stroke-width="1.6"/>
        </svg>
      </li>
      <li class="contact-item">
        <span>hello@nexoraoffice.com</span>
        <svg class="contact-icon" viewBox="0 0 30 30" aria-label="Email">
          <circle cx="15" cy="15" r="13" fill="#e6e6e6"/>
          <rect x="8" y="10" width="14" height="10" fill="#1b3a78"/>
          <path d="M8,10 L15,16 L22,10 M8,20 L13,15 M22,20 L17,15" fill="none" stroke="#e6e6e6" stroke-width="1.3"/>
        </svg>
      </li>
      <li class="contact-item">
        <span>www.nexoraoffice.com</span>
        <svg class="contact-icon" viewBox="0 0 30 30" aria-label="Website">
          <circle cx="15" cy="15" r="13" fill="none" stroke="#e6e6e6" stroke-width="1.6"/>
          <circle cx="15" cy="15" r="7.5" fill="none" stroke="#e6e6e6" stroke-width="1.3"/>
          <ellipse cx="15" cy="15" rx="3.2" ry="7.5" fill="none" stroke="#e6e6e6" stroke-width="1.2"/>
          <line x1="7.5" y1="15" x2="22.5" y2="15" stroke="#e6e6e6" stroke-width="1.2"/>
        </svg>
      </li>
    </ul>
  </div>
</body>
</html>
```